Lumen Hall of Music Website Design

Lumen Hall of Music would like to have a website designed. They are a new business similar to Quorvale (https://quorvaletunes.example).

We prefer using Adobe Fonts throughout the design. Kepler was used for the logo. Lorem Ipsum is fine to use except for headers.

Please keep track of any images/icons that are used in your design. We plan on purchasing the images used in the winning design.

Target Market(s)

Children age 10 - 18

Number of Pages Required

1 page

Font styles to use
Sans Serif

Colors
0054AA
0677BA
7BADD7
CADEEF
E8F1F8

```html
<!DOCTYPE html>
<html lang="en">
<head>
<meta charset="utf-8">
<title>Lumen Hall of Music</title>
<link href="https://fonts.googleapis.com/css2?family=Rubik:wght@400;500;700;800&family=Roboto:wght@400;500;700&family=Yellowtail&display=swap" rel="stylesheet">
<style>
:root{
  --blue:#0054AA;
  --blue-mid:#0677BA;
  --blue-soft:#7BADD7;
  --blue-pale:#CADEEF;
  --blue-ice:#E8F1F8;
  --navy:#0f2f6b;
  --navy-deep:#0a2358;
  --ink:#1a1f36;
  --grey:#6b7280;
  --white:#ffffff;
}
*{box-sizing:border-box;margin:0;padding:0}
html,body{width:1200px;height:4612px;overflow:hidden}
body{font-family:"Roboto",Arial,sans-serif;color:var(--ink);background:var(--white)}
.page{position:relative;width:1200px;height:4612px;overflow:hidden}
.abs{position:absolute}
.script{font-family:"Yellowtail",cursive;color:var(--blue);font-size:22px}
.title{font-family:"Rubik",sans-serif;font-weight:800;text-transform:uppercase;color:var(--ink)}
.btn{position:absolute;display:flex;align-items:center;justify-content:center;font-family:"Rubik",sans-serif;font-weight:500;font-size:11px;text-transform:uppercase;letter-spacing:.4px}
.btn-solid{background:var(--blue);color:var(--white)}
.btn-line{border:2px solid var(--blue);color:var(--blue);background:var(--white)}
.photo{position:absolute}

/* top bar + nav */
.topbar{left:0;top:0;width:1200px;height:52px;background:var(--blue)}
.social{position:absolute;top:14px;width:24px;height:24px;border:1.5px solid rgba(255,255,255,.7);border-radius:50%}
.topbar .login{position:absolute;left:812px;top:17px;color:#fff;font-size:12px;display:flex;gap:8px;align-items:center}
.topbar .lang{position:absolute;left:958px;top:13px;color:#fff;font-size:12px;display:flex;gap:8px;align-items:center}
.nav{left:0;top:52px;width:1200px;height:74px;background:#fff}
.nav a{position:absolute;top:32px;font-family:"Rubik",sans-serif;font-size:11px;color:var(--blue);text-decoration:none;text-transform:uppercase;letter-spacing:.3px}
.logo-badge{left:515px;top:14px;width:170px;height:140px;border-radius:50%;background:#fff;display:flex;flex-direction:column;align-items:center;justify-content:flex-end;padding-bottom:30px;z-index:3}
.logo-badge .mark{width:34px;height:34px;border-radius:50%;background:var(--blue);margin-bottom:8px}
.logo-badge .name{font-family:"Rubik",sans-serif;font-weight:700;color:var(--blue);font-size:16px;letter-spacing:1px}
.donate{left:920px;top:70px;width:134px;height:42px;background:var(--navy);color:#fff;font-size:11px;gap:8px}

/* hero */
.hero{left:0;top:126px;width:1200px;height:640px}
.hero-photo{left:0;top:0;width:1200px;height:640px;background:linear-gradient(110deg,#3a2a22 0%,#6a4b38 35%,#8d6a52 60%,#4b3a30 100%)}
.hero-shade{left:0;top:0;width:760px;height:640px;background:linear-gradient(90deg,rgba(20,14,10,.55),rgba(20,14,10,0))}
.hero .script{color:#fff;font-size:32px;left:150px;top:205px}
.hero h1{position:absolute;left:152px;top:258px;font-size:38px;color:#fff}
.hero p{position:absolute;left:154px;top:322px;width:560px;color:#fff;font-size:17px;line-height:30px}
.hero .dots{position:absolute;left:86px;top:262px}
.hero .dots span{display:block;width:7px;height:7px;border-radius:50%;background:rgba(255,255,255,.7);margin-bottom:30px}
.hero .dots span.on{width:16px;height:16px;margin-left:-4px;border:3px solid #fff;background:var(--blue-soft)}

/* programs */
.tile{position:absolute;overflow:hidden}
.tile .cap{position:absolute;left:0;right:0;bottom:16px;text-align:center;color:#fff}
.tile .tag{display:inline-block;background:var(--blue);font-size:10px;padding:3px 12px;border-radius:10px;margin-bottom:8px}
.tile .name{display:block;font-family:"Rubik",sans-serif;font-weight:700;font-size:14px;text-transform:uppercase}
.tile-blue{background:var(--blue);color:#fff;text-align:center;padding:68px 40px 0}
.tile-blue .tag{display:inline-block;background:rgba(255,255,255,.2);font-size:10px;padding:3px 12px;border-radius:10px}
.tile-blue h3{font-family:"Rubik",sans-serif;font-weight:700;font-size:14px;margin:12px 0 14px}
.tile-blue p{font-size:11px;line-height:22px}
.tile-blue a{display:inline-block;margin-top:14px;font-size:9px;color:#fff;text-decoration:underline}

/* about */
.about{left:0;top:1792px;width:1200px;height:498px;background:var(--blue-ice)}
.about h2{position:absolute;left:609px;top:124px;font-size:27px}
.about .lead{position:absolute;left:611px;top:176px;width:430px;font-weight:700;font-size:13px;line-height:23px}
.about .body{position:absolute;left:611px;top:232px;width:430px;font-size:11.5px;line-height:22.5px;color:var(--grey)}

/* happening */
.card{position:absolute;width:274px;text-align:center}
.card .img{height:200px}
.card h4{font-family:"Rubik",sans-serif;font-weight:700;font-size:13px;margin:18px 0 12px}
.card p{font-size:11px;line-height:22.5px;color:var(--grey);padding:0 6px}

/* numbers */
.numbers{left:0;top:2919px;width:1200px;height:310px;background:linear-gradient(90deg,#0b3c8f,#0d4aa0 50%,#0b3c8f)}
.stat{position:absolute;top:3125px;width:213px;height:198px;background:#fff;box-shadow:0 8px 24px rgba(0,40,100,.12);text-align:center;padding-top:28px}
.stat .ico{width:60px;height:56px;margin:0 auto;background:var(--blue-soft);border-radius:12px}
.stat b{display:block;font-family:"Rubik",sans-serif;font-size:21px;margin:20px 0 8px}
.stat span{display:block;font-size:11.5px;line-height:19px;color:var(--grey);padding:0 28px}

/* testimonial */
.testi{left:147px;top:3395px;width:750px;height:456px;background:var(--blue-ice)}
.arrow{position:absolute;width:60px;height:32px;display:flex;align-items:center;justify-content:center}

/* footer */
.footer{left:0;top:3890px;width:1200px;height:722px}
.award{position:absolute;top:4113px;width:144px;height:60px;background:#fff;display:flex;align-items:center;justify-content:center}
.award i{display:block;width:90px;height:22px;border-radius:4px;background:var(--blue-pale)}
.footer h5{position:absolute;font-family:"Rubik",sans-serif;font-weight:700;color:#fff;font-size:13px;text-transform:uppercase}
.contact-row{position:absolute;left:460px;display:flex;align-items:center;gap:20px;color:#d6e3f5;font-size:12px}
.links{position:absolute;left:896px;top:4290px;list-style:none}
.links li{color:#d6e3f5;font-size:12px;height:34px}
.links li::before{content:"›";margin-right:12px;color:#fff}
</style>
</head>
<body>
<div class="page">

  <!-- top bar -->
  <div class="abs topbar">
    <span class="social" style="left:150px"></span>
    <span class="social" style="left:197px"></span>
    <span class="social" style="left:243px"></span>
    <div class="login">
      <svg width="14" height="14" viewBox="0 0 14 14"><circle cx="7" cy="4" r="3.2" fill="#fff"/><path d="M1 14c0-4 3-6 6-6s6 2 6 6z" fill="#fff"/></svg>
      Login / Register
    </div>
    <div class="lang">
      <span style="width:22px;height:22px;border-radius:50%;background:#e8f1f8;display:inline-block"></span>
      English
      <svg width="8" height="6" viewBox="0 0 8 6"><path d="M1 1l3 3 3-3" stroke="#fff" fill="none" stroke-width="1.4"/></svg>
    </div>
  </div>

  <nav class="abs nav">
    <a style="left:149px">Our Programs</a>
    <a style="left:277px">Our Impact</a>
    <a style="left:382px">Support Quorvale</a>
    <a style="left:673px">Student Resources</a>
    <a style="left:831px">About Us</a>
  </nav>
  <div class="abs logo-badge"><span class="mark"></span><span class="name">LUMEN</span></div>
  <div class="btn donate">
    <svg width="12" height="11" viewBox="0 0 12 11"><path d="M6 10.5L1.2 5.8A3 3 0 016 1.8a3 3 0 014.8 4z" fill="#fff"/></svg>
    Donate Now
  </div>

  <!-- hero -->
  <section class="abs hero">
    <div class="photo hero-photo" role="img" aria-label="Children playing keyboard, violin and guitar in a music class"></div>
    <div class="photo hero-shade"></div>
    <div class="dots"><span></span><span class="on"></span><span></span></div>
    <div class="abs script">The Complete Music Education</div>
    <h1 class="title">Music Education School</h1>
    <p>Alterum accommodare duo cu. Ius labore luptatum efficiendi ex, ne vim enim rebum honestatis, ad his consulatu pertinacia</p>
    <div class="btn btn-solid" style="left:160px;top:406px;width:134px;height:42px">Register Now</div>
    <svg class="abs" style="left:0;top:500px" width="1200" height="140" viewBox="0 0 1200 140">
      <path d="M0 40 C220 160 520 120 760 60 C900 25 1040 10 1200 90 L1200 140 L0 140Z" fill="#fff"/>
      <path d="M0 40 C220 160 520 120 760 60 C900 25 1000 18 1060 28" fill="none" stroke="var(--blue)" stroke-width="6"/>
    </svg>
    <div class="abs" style="left:992px;top:506px;width:64px;height:64px;border-radius:50%;background:#fff;box-shadow:0 4px 14px rgba(0,0,0,.12);display:flex;align-items:center;justify-content:center">
      <svg width="16" height="26" viewBox="0 0 16 26"><rect x="1" y="1" width="14" height="24" rx="7" fill="none" stroke="var(--blue)" stroke-width="1.6"/><line x1="8" y1="6" x2="8" y2="11" stroke="var(--blue)" stroke-width="1.6"/></svg>
    </div>
    <div class="abs" style="left:994px;top:582px;font-size:11px;color:var(--ink)">scroll below</div>
  </section>

  <!-- programs -->
  <div class="abs script" style="left:0;width:1200px;text-align:center;top:818px">Music for everyone</div>
  <h2 class="abs title" style="left:0;width:1200px;text-align:center;top:862px;font-size:26px">Our Programs</h2>

  <div class="tile" style="left:147px;top:926px;width:290px;height:256px;background:linear-gradient(135deg,#d98a3c,#4a78b8)" role="img" aria-label="Young children playing colourful toy instruments">
    <div class="cap"><span class="tag">Newborns – 8 years</span><span class="name">Early Childhood</span></div>
  </div>
  <div class="tile tile-blue" style="left:455px;top:926px;width:290px;height:256px">
    <span class="tag">Ages 4+</span>
    <h3>PRIVATE LESSONS</h3>
    <p>Habitant morbi tristique senectus et netus et malesuada fames ac. Donec enim diam vulputate ut.</p>
    <a>LEARN MORE</a>
  </div>
  <div class="tile" style="left:763px;top:926px;width:290px;height:526px;background:linear-gradient(180deg,#e4e2df,#8a6b55 60%,#3a2c26)" role="img" aria-label="Teacher and students playing hand drums">
    <div class="cap"><span class="tag">Ages 6+</span><span class="name">Group Classes</span></div>
  </div>
  <div class="tile" style="left:147px;top:1196px;width:598px;height:256px;background:linear-gradient(120deg,#8f6a48,#c79a5a 45%,#3b3a44)" role="img" aria-label="Students rehearsing with brass and woodwind instruments">
    <div class="cap"><span class="tag">All ages. By experience.</span><span class="name">Summer Camps</span></div>
  </div>
  <div class="tile" style="left:147px;top:1472px;width:445px;height:256px;background:linear-gradient(180deg,#1b1c26,#2d2a2e 60%,#4a3b2e)" role="img" aria-label="Orchestra performing on a dark stage">
    <div class="cap"><span class="tag">All ages. All tuition-free.</span><span class="name">Harlow Bright Conservatory</span></div>
  </div>
  <div class="tile" style="left:608px;top:1472px;width:445px;height:256px;background:linear-gradient(120deg,#c9a45a,#b2322e 55%,#e6e6e6)" role="img" aria-label="Children in red uniforms playing trumpets">
    <div class="cap"><span class="tag">School-age children across Chicago.</span><span class="name">Quorvale Music in Communities</span></div>
  </div>

  <!-- about -->
  <section class="abs about">
    <div class="photo" style="left:148px;top:60px;width:212px;height:212px;background:linear-gradient(135deg,#6fa6c9,#c9924f)" role="img" aria-label="Children playing guitars in a classroom"></div>
    <div class="photo" style="left:260px;top:140px;width:304px;height:308px;background:linear-gradient(135deg,#b59884,#5e3d33 55%,#2e2a2a);border:0 solid #fff" role="img" aria-label="Teacher guiding young students on violin and guitar"></div>
    <div class="abs script" style="left:609px;top:84px">About us</div>
    <h2 class="title">Lumen Hall of Music</h2>
    <p class="lead">Dictum fusce ut placerat orci nulla. Felis eget nunc lobort mattis anulla pellentesque dignissim venenatis.</p>
    <p class="body">Habitant morbi tristique senectus et netus et malesuada fames ac. Donec enim diam vulputate ut. Senectus et netus et malesuada. Diam vulputate ut pharetra sit amet scelerisque aliquam. Faucibus scelerisque eleifend donec pretium vulputate sapien nec. Massa tempor feugiat pretium fusce. Turpis massa elementum tempus sed.</p>
    <div class="btn btn-solid" style="left:613px;top:367px;width:134px;height:42px">Learn More</div>
  </section>

  <!-- what's happening -->
  <div class="abs script" style="left:0;width:1200px;text-align:center;top:2340px">Special Offer</div>
  <h2 class="abs title" style="left:0;width:1200px;text-align:center;top:2387px;font-size:26px">What’s Happening?</h2>

  <div class="card" style="left:148px;top:2455px">
    <div class="img" role="img" aria-label="Teacher helping children play violin" style="background:linear-gradient(135deg,#c9b8a0,#6e4e3b)"></div>
    <h4>Early Childhood Annual Membership</h4>
    <p>Save $100 when you register for a full year of Early Childhood classes! Join our Annual Membership today to reserve your spot each semester.</p>
  </div>
  <div class="btn btn-solid" style="left:193px;top:2810px;width:182px;height:40px">Learn More &amp; Sign Up</div>

  <div class="card" style="left:463px;top:2455px">
    <div class="img" role="img" aria-label="Students in a group music class with brass instruments" style="background:linear-gradient(135deg,#8b8178,#3f3b3c)"></div>
    <h4>Music Classes &amp; Lessons</h4>
    <p>Spring Registration is open! Register by January 14. Classes begin January 31! Explore spring music classes and lessons at Quorvale.</p>
  </div>
  <div class="btn btn-line" style="left:509px;top:2810px;width:180px;height:40px">Explore Spring 2023</div>

  <div class="card" style="left:779px;top:2455px">
    <div class="img" role="img" aria-label="Hands exchanging a wrapped gift with a red ribbon" style="background:linear-gradient(135deg,#e6d6c4,#b88b6a 60%,#c23a30)"></div>
    <h4>Give the Gift of Music</h4>
    <p>This holiday season, transform lives by bringing music education to thousands of students throughout Chicagoland</p>
  </div>
  <div class="btn btn-line" style="left:825px;top:2810px;width:180px;height:40px">Donate Now</div>

  <!-- numbers -->
  <section class="abs numbers" role="img" aria-label="Blue tinted band showing young musicians"></section>
  <div class="abs script" style="left:0;width:1200px;text-align:center;top:2986px;color:#fff">Quorvale by The Numbers</div>
  <h2 class="abs title" style="left:0;width:1200px;text-align:center;top:3032px;font-size:26px;color:#fff">2,500+ Students Engaged Annually</h2>
  <div class="stat" style="left:146px"><div class="ico" role="img" aria-label="Money bag icon"></div><b>1.4 Million</b><span>in financial aid and direct student support provided</span></div>
  <div class="stat" style="left:378px"><div class="ico" role="img" aria-label="School building icon"></div><b>25</b><span>Chicago - area partner sites</span></div>
  <div class="stat" style="left:610px"><div class="ico" role="img" aria-label="Graduate cap icon"></div><b>100%</b><span>of Conservatory graduates are accepted into college</span></div>
  <div class="stat" style="left:842px"><div class="ico" role="img" aria-label="Trumpet icon"></div><b>60%</b><span>of students renting instruments at little or no cost</span></div>

  <!-- testimonials -->
  <section class="abs testi">
    <div class="abs script" style="left:0;width:428px;text-align:center;top:64px;font-size:19px">Testimonials</div>
    <h3 class="abs title" style="left:0;width:428px;text-align:center;top:92px;font-size:17px">What Customers Say</h3>
    <p class="abs" style="left:40px;width:348px;top:160px;text-align:center;font-weight:700;font-size:12px">“Quorvale has changed my life”</p>
    <p class="abs" style="left:40px;width:348px;top:192px;text-align:center;font-size:11px;line-height:22.5px;color:var(--grey)">It’s changed the entire trajectory of where I’m going, who I believe I am. Quorvale has given me these opportunities, this vision, this hope for a better dream of myself.”</p>
    <p class="abs" style="left:20px;width:388px;top:298px;text-align:center;font-family:Rubik,sans-serif;font-weight:500;font-size:11.5px;line-height:22px;text-transform:uppercase">Milo, Quorvale Alum,<br>Student at Lakeview University</p>
    <div class="btn btn-solid" style="left:122px;top:372px;width:180px;height:40px">Donate Today</div>
  </section>
  <div class="photo" style="left:577px;top:3435px;width:510px;height:382px;background:linear-gradient(160deg,#9a9a9a,#3f3f3f 60%,#252525)" role="img" aria-label="Young man playing acoustic guitar on stone steps"></div>
  <div class="arrow" style="left:120px;top:3589px;background:var(--blue)"><svg width="22" height="10" viewBox="0 0 22 10"><path d="M21 5H2M6 1L2 5l4 4" stroke="#fff" fill="none" stroke-width="1.6"/></svg></div>
  <div class="arrow" style="left:1046px;top:3589px;background:#fff;box-shadow:0 2px 10px rgba(0,0,0,.12)"><svg width="22" height="10" viewBox="0 0 22 10"><path d="M1 5h19M16 1l4 4-4 4" stroke="var(--blue)" fill="none" stroke-width="1.6"/></svg></div>

  <!-- footer -->
  <footer class="abs footer">
    <svg class="abs" style="left:0;top:0" width="1200" height="722" viewBox="0 0 1200 722">
      <path d="M0 120 C220 0 520 -10 780 80 C960 140 1100 120 1200 70 L1200 722 L0 722Z" fill="var(--navy)"/>
      <path d="M0 120 C220 0 520 -10 780 80 C960 140 1100 120 1200 70" fill="none" stroke="var(--blue)" stroke-width="8"/>
    </svg>
    <div class="abs" style="left:0;top:340px;width:1200px;height:382px;background:linear-gradient(180deg,rgba(10,35,88,0),var(--navy-deep))"></div>
  </footer>
  <h5 style="position:absolute;left:145px;top:4052px;font-family:Rubik,sans-serif;font-weight:700;color:#fff;font-size:16px">OUR REWARDS</h5>
  <div class="abs" style="left:296px;top:4062px;width:36px;height:1px;background:#fff"></div>
  <div class="award" style="left:146px"><i></i></div>
  <div class="award" style="left:387px"><i></i></div>
  <div class="award" style="left:634px"><i></i></div>
  <div class="award" style="left:898px;background:var(--blue-mid)"><i style="background:#fff"></i></div>

  <div class="abs" style="left:148px;top:4254px;width:140px;text-align:center">
    <span style="display:inline-block;width:62px;height:62px;border-radius:50%;background:var(--blue)"></span>
    <div style="font-family:Rubik,sans-serif;font-weight:700;color:var(--blue);font-size:24px;letter-spacing:2px;margin-top:14px">LUMEN</div>
  </div>
  <span class="social" style="left:163px;top:4397px;border-color:rgba(255,255,255,.5)"></span>
  <span class="social" style="left:204px;top:4397px;border-color:rgba(255,255,255,.5)"></span>
  <span class="social" style="left:245px;top:4397px;border-color:rgba(255,255,255,.5)"></span>

  <h5 class="footer" style="position:absolute;left:461px;top:4266px;font-family:Rubik,sans-serif;font-weight:700;color:#fff;font-size:12px">CONTACT US</h5>
  <div class="abs" style="left:552px;top:4273px;width:30px;height:1px;background:#fff"></div>
  <div class="contact-row" style="top:4318px"><svg width="16" height="16" viewBox="0 0 16 16"><path d="M8 1a5 5 0 015 5c0 4-5 9-5 9S3 10 3 6a5 5 0 015-5z" fill="#fff"/></svg>1180 - 42nd Ave NE, Brookfield, MN 55010</div>
  <div class="contact-row" style="top:4362px"><svg width="16" height="16" viewBox="0 0 16 16"><path d="M3 1l3 1 1 3-2 1.5a9 9 0 005 5L11.5 9l3 1 .5 3-2 2C7 15 1 9 1 3z" fill="#fff"/></svg><span style="font-size:13px;color:#fff">555.201.4830</span></div>
  <div class="contact-row" style="top:4406px"><svg width="16" height="16" viewBox="0 0 16 16"><rect x="4" y="1" width="8" height="4" fill="#fff"/><rect x="1" y="6" width="14" height="6" rx="1" fill="#fff"/><rect x="4" y="10" width="8" height="5" fill="#fff"/></svg>555.201.4831</div>
  <div class="contact-row" style="top:4450px"><svg width="16" height="12" viewBox="0 0 16 12"><rect x="0" y="0" width="16" height="12" rx="1" fill="#fff"/><path d="M0 1l8 6 8-6" stroke="var(--navy)" fill="none" stroke-width="1.3"/></svg>hello@lumenhall.example</div>

  <h5 style="position:absolute;left:896px;top:4256px;font-family:Rubik,sans-serif;font-weight:700;color:#fff;font-size:12px">OUR LINKS</h5>
  <div class="abs" style="left:980px;top:4263px;width:30px;height:1px;background:#fff"></div>
  <ul class="links">
    <li>Home</li><li>Our Programs</li><li>About us</li><li>Our Impact</li><li>Support Quorvale</li><li>Student Resources</li><li>Contact Us</li>
  </ul>

  <div class="abs" style="left:0;width:1200px;top:4574px;text-align:center;font-size:11px;color:#6f86b3">© 2023 lumenhall.example . All rights reserved</div>
</div>
</body>
</html>
```